Free Shipping on Orders of $50 and Over

Ideally, I would like a HTML5 banner for the homepage of https://www.1866lumoravex.com showing free shipping for orders of $50 or more. If there are some ways to make it with moving elements, like something using HTML5, that would be better.

The theme on the site using WP Bakery (Wordpress) and can be built with that plugin, or with HTML5 or a simple jpg.
Updates

To clarify, it does not have to be in HTML5. I would like some animation but it is not mandatory. Video or gif is okay too,.

Industry/Entity Type

Home And Garden

Font styles to use
Sans Serif

Requirements
Must have
• orders $50 or more
domestic usa only
Nice to have
• something that moves. Would be great if I could use this same banner through black Friday, Cyber Monday, etc.
Should not have
• colors that clash with current website colors

```html
<!DOCTYPE html>
<html lang="en">
<head>
<meta charset="utf-8">
<title>Free Shipping – Lumoravex</title>
<link rel="stylesheet" href="https://fonts.googleapis.com/css2?family=Bebas+Neue&family=Montserrat:ital,wght@0,700;0,800;1,800&display=swap">
<style>
  :root {
    --bg: #f2f2f2;
    --brand-blue: #0a86d1;
    --ink: #0b0b0b;
    --white: #ffffff;
    --mark-grey: #5a5a5a;
    --art-light: #e9e3d6;
    --art-mid: #c9ac7c;
  }
  html, body {
    margin: 0;
    padding: 0;
    overflow: hidden;
    background: var(--bg);
  }
  .banner {
    position: relative;
    width: 1200px;
    height: 675px;
    overflow: hidden;
    background: var(--bg);
  }
  .banner__art {
    position: absolute;
    left: 68px;
    top: 84px;
    width: 392px;
    height: 486px;
    border-radius: 36px;
    background: linear-gradient(160deg, var(--white) 0%, var(--art-light) 45%, var(--art-mid) 100%);
  }
  .banner__graphics {
    position: absolute;
    inset: 0;
    width: 1200px;
    height: 675px;
  }
  .offer-tag {
    font-family: "Montserrat", sans-serif;
    font-weight: 800;
    font-style: italic;
    font-size: 21px;
    fill: var(--white);
  }
  .headline {
    font-family: "Bebas Neue", sans-serif;
    font-size: 96px;
    fill: var(--white);
  }
  .subline {
    font-family: "Montserrat", sans-serif;
    font-weight: 800;
    font-size: 19px;
    letter-spacing: 2px;
    fill: var(--brand-blue);
  }
  .note {
    font-family: "Montserrat", sans-serif;
    font-weight: 700;
    font-size: 16px;
    letter-spacing: 1px;
    fill: var(--white);
  }
  .cta-label {
    font-family: "Montserrat", sans-serif;
    font-weight: 800;
    font-size: 16px;
    letter-spacing: 2px;
    fill: var(--ink);
  }
  .accent-blue { fill: var(--brand-blue); }
  .accent-ink { fill: var(--ink); }
  .marker { fill: none; stroke: var(--mark-grey); stroke-width: 3; }
  .cross { stroke: var(--mark-grey); stroke-width: 3; stroke-linecap: round; }
</style>
</head>
<body>
  <main class="banner">
    <div class="banner__art" role="img" aria-label="Smartphone showing a delivery app with a check mark, a cardboard parcel stamped Shipped from 1866LUMORAVEX flying out of the screen, and stacked parcels beside it"></div>

    <svg class="banner__graphics" viewBox="0 0 1200 675" aria-hidden="false">
      <defs>
        <radialGradient id="floor-shadow" cx="50%" cy="50%" r="50%">
          <stop offset="0%" stop-color="#9a9a9a" stop-opacity="0.75"/>
          <stop offset="100%" stop-color="#f2f2f2" stop-opacity="0"/>
        </radialGradient>
        <radialGradient id="halftone-haze" cx="50%" cy="50%" r="50%">
          <stop offset="0%" stop-color="#d4d4d4" stop-opacity="0.8"/>
          <stop offset="100%" stop-color="#f2f2f2" stop-opacity="0"/>
        </radialGradient>
      </defs>

      <!-- soft texture behind the headline -->
      <ellipse role="img" aria-label="Halftone dot texture" cx="640" cy="250" rx="130" ry="90" fill="url(#halftone-haze)"/>
      <ellipse role="img" aria-label="Halftone dot texture" cx="1030" cy="215" rx="110" ry="60" fill="url(#halftone-haze)"/>
      <ellipse role="img" aria-label="Concentric ring texture" cx="985" cy="425" rx="60" ry="40" fill="url(#halftone-haze)"/>

      <!-- floor shadow under the call to action -->
      <ellipse cx="825" cy="552" rx="270" ry="14" fill="url(#floor-shadow)"/>

      <!-- accent triangles -->
      <polygon class="accent-blue" points="652,397 718,391 686,414"/>
      <polygon class="accent-blue" points="1068,282 1130,276 1108,312"/>

      <!-- lower blue band -->
      <polygon class="accent-blue" points="728,372 1090,355 1078,408 738,411"/>
      <text class="note" x="780" y="393">*Domestic USA Only</text>

      <!-- main black banner -->
      <polygon class="accent-ink" points="559,250 1106,215 1072,360 621,375"/>
      <text class="headline" x="825" y="329" text-anchor="middle" textLength="432" lengthAdjust="spacingAndGlyphs">FREE SHIPPING</text>
      <text class="subline" x="828" y="362" text-anchor="middle" textLength="382" lengthAdjust="spacingAndGlyphs">FOR ORDERS $50 AND OVER</text>

      <!-- offer tag -->
      <polygon class="accent-blue" points="535,220 782,188 765,244 535,251"/>
      <text class="offer-tag" x="560" y="242" transform="rotate(-5 560 242)">Offer end Dec 1st</text>

      <!-- markers -->
      <circle class="marker" cx="636" cy="412" r="5"/>
      <circle class="marker" cx="1098" cy="391" r="5"/>
      <line class="cross" x1="672" y1="420" x2="682" y2="430"/>
      <line class="cross" x1="682" y1="420" x2="672" y2="430"/>
      <line class="cross" x1="1066" y1="420" x2="1076" y2="430"/>
      <line class="cross" x1="1076" y1="420" x2="1066" y2="430"/>

      <!-- call to action -->
      <a href="https://www.1866lumoravex.com" class="cta">
        <polygon points="748,477 915,477 904,512 737,512" fill="var(--white)" stroke="var(--ink)" stroke-width="4"/>
        <text class="cta-label" x="826" y="501" text-anchor="middle">SHOP NOW</text>
      </a>
    </svg>
  </main>
</body>
</html>
```